Post Card (5x7) - Pre-foreclosure Image - Harbor Path Partners

(Two-Sided Post Card)
FACING FORECLOSURE? YOU STILL HAVE OPTIONS.
If you’re behind on payments or at risk of foreclosure, you’re not alone—and it’s not too late to take action.
We help homeowners:
• Explore options to stay in their home
• Stop or delay foreclosure
• Sell quickly for a fair price if needed
No pressure. No obligation. Just real solutions tailored to your situation.
Call - (240) 558-2094
Email - marcus@hpbllc-mail.com
Harbor Path Partners LLC
7200 Bramwick Lane, Ellicott City, MD 21043
**Marcus Fennimore is a Licensed Realtor with Copperleaf Homes Realty in Bethesda, Maryland.
(Leave room for mailing address, return address & postage)
Target Market(s)
Distressed Homeowners
Industry/Entity Type
Real Estate

```html
<!DOCTYPE html>
<html lang="en">
<head>
<meta charset="utf-8">
<title>Harbor Path Partners – Pre-foreclosure Postcard</title>
<link href="https://fonts.googleapis.com/css2?family=Montserrat:wght@500;600;700;800;900&family=Figtree:wght@400;500;600&family=Oswald:wght@600&display=swap" rel="stylesheet">
<style>
  :root{
    --stage:#adadad;
    --stage-label:#c9c9c9;
    --orange:#f57c12;
    --black:#000;
    --ink:#111;
    --white:#fff;
    --rule:#9a9a9a;
    --stamp:#d9d9d9;
    --panel:#efefef;
  }
  *{box-sizing:border-box;margin:0;padding:0}
  html,body{width:890px;height:1200px;overflow:hidden;background:var(--stage)}
  .canvas{position:relative;width:890px;height:1200px;background:var(--stage);font-family:"Figtree",sans-serif;color:var(--ink)}
  .side-label{position:absolute;left:57px;transform:translate(-50%,-50%) rotate(-90deg);font-family:"Montserrat",sans-serif;font-weight:500;font-size:34px;letter-spacing:2px;color:var(--stage-label);white-space:nowrap}
  .side-label.front{top:320px}
  .side-label.back{top:892px}

  .card{position:absolute;left:109px;width:736px;height:526px;overflow:hidden}
  .card.front{top:58px;background:var(--black)}
  .card.back{top:617px;background:var(--white)}

  /* FRONT */
  .hero{position:absolute;left:0;top:0;width:736px;height:443px;
    background:linear-gradient(180deg,#35345f 0%,#6b4a78 14%,#c25a6e 28%,#a65a55 44%,#5b4a4a 58%,#3a3036 70%,#1b1518 82%,#000 100%)}
  .brand{position:absolute;left:0;right:0;text-align:center;color:var(--white);font-family:"Montserrat",sans-serif;font-weight:600}
  .front .brand{top:78px}
  .brand .name{font-size:21px;letter-spacing:3.5px;line-height:1.1}
  .brand .llc{font-size:12px;letter-spacing:4px;margin-top:3px}
  .headline{position:absolute;left:0;right:0;text-align:center;font-family:"Montserrat",sans-serif;font-weight:800;line-height:1}
  .headline.primary{top:293px;font-size:41px;color:var(--white)}
  .headline.accent{top:339px;font-size:43px;color:var(--orange)}
  .lede{position:absolute;left:0;right:0;top:389px;text-align:center;color:var(--white);font-size:14.5px;line-height:17.5px}
  .contact-band{position:absolute;left:0;top:443px;width:736px;height:83px;border-top:1.5px solid #555;background:var(--black);color:var(--white)}
  .contact-band .phone-icon{position:absolute;left:32px;top:23px}
  .contact-band .phone{position:absolute;left:80px;top:19px;font-family:"Montserrat",sans-serif;font-weight:700;font-size:33px;letter-spacing:.5px}
  .contact-band .divider{position:absolute;left:341px;top:21px;width:1px;height:36px;background:#888}
  .contact-band .pin{position:absolute;left:354px;top:23px}
  .contact-band .address{position:absolute;left:380px;top:20px;font-size:14px;line-height:17px}
  .contact-band .mail{position:absolute;left:537px;top:23px}
  .contact-band .email{position:absolute;left:567px;top:20px;font-size:14px;line-height:17px}

  /* BACK */
  .help-title{position:absolute;left:48px;top:28px;font-family:"Montserrat",sans-serif;font-weight:800;font-size:29px}
  .help-title span{color:var(--orange)}
  .service-icon{position:absolute;top:84px}
  .connector{position:absolute;top:96px}
  .service-label{position:absolute;top:144px;width:120px;margin-left:-60px;text-align:center;font-size:15px;line-height:17.5px;font-weight:500}
  .section-rule{position:absolute;left:32px;top:219px;width:372px;height:1px;background:#c8c8c8}
  .section-split{position:absolute;left:268px;top:220px;width:1px;height:109px;background:#c8c8c8}
  .agent-photo{position:absolute;left:33px;top:233px;width:90px;height:90px;border-radius:50%;background:radial-gradient(circle at 50% 40%,#d6d6d6 0%,#a9a9a9 60%,#6d6d6d 100%)}
  .agent-name{position:absolute;left:143px;top:245px;font-family:"Oswald",sans-serif;font-weight:600;font-size:19px;color:var(--orange);letter-spacing:-.2px}
  .agent-bio{position:absolute;left:143px;top:272px;font-size:12.3px;line-height:14px;width:118px}
  .promise{position:absolute;left:284px;top:250px;font-size:12.3px;line-height:14px;width:118px;font-weight:500}
  .skyline-panel{position:absolute;left:0;top:341px;width:405px;height:185px;background:linear-gradient(180deg,#fbfbfb 0%,var(--panel) 45%,var(--panel) 100%)}
  .back .phone-icon{position:absolute;left:33px;top:442px}
  .back .phone{position:absolute;left:84px;top:437px;font-family:"Montserrat",sans-serif;font-weight:700;font-size:36px;color:var(--ink)}
  .back .phone-rule{position:absolute;left:33px;top:483px;width:336px;height:1px;background:#cfcfcf}
  .back .pin{position:absolute;left:33px;top:489px}
  .back .address{position:absolute;left:59px;top:490px;font-size:15px;font-weight:500}
  .stamp-box{position:absolute;left:608px;top:34px;width:95px;height:117px;background:var(--stamp)}
  .mail-line{position:absolute;left:453px;width:251px;height:1.5px;background:var(--rule)}
  .back .brand{color:var(--ink);left:453px;right:32px;top:455px}
  .back .brand .name{font-size:21px;letter-spacing:3px}
</style>
</head>
<body>
<div class="canvas">
  <div class="side-label front">FRONT PAGE</div>
  <div class="side-label back">BACK PAGE</div>

  <section class="card front">
    <div class="hero" role="img" aria-label="Photograph of a waterfront city skyline at sunset with a pink and purple sky"></div>
    <div class="brand">
      <div class="name">HARBOR PATH PARTNERS</div>
      <div class="llc">LLC</div>
    </div>
    <h1 class="headline primary">FACING FORECLOSURE?</h1>
    <h2 class="headline accent">YOU STILL HAVE OPTIONS</h2>
    <p class="lede">If you’re behind on payments or at risk of foreclosure, you’re not<br>alone—and it’s not too late to take action.</p>

    <div class="contact-band">
      <svg class="phone-icon" width="38" height="36" viewBox="0 0 38 36"><path d="M0 0H38V26L19 36L0 26Z" fill="#f57c12"/><path d="M13 9c-2 1-3 3-1 7s6 8 9 9c2 1 4 0 5-2l-3-3-2 1c-2-1-4-3-5-5l1-2z" fill="#fff"/></svg>
      <div class="phone">(240) 558-2094</div>
      <div class="divider"></div>
      <svg class="pin" width="18" height="17" viewBox="0 0 18 17"><path d="M0 0H18V12L9 17L0 12Z" fill="#f57c12"/><circle cx="9" cy="7" r="3.2" fill="none" stroke="#fff" stroke-width="1.6"/></svg>
      <div class="address">7200 Bramwick Lane,<br>Ellicott City, MD 21043</div>
      <svg class="mail" width="18" height="17" viewBox="0 0 18 17"><path d="M0 0H18V12L9 17L0 12Z" fill="#f57c12"/><rect x="4" y="4" width="10" height="7" fill="#fff"/><path d="M4 4l5 4 5-4" fill="none" stroke="#f57c12" stroke-width="1"/></svg>
      <div class="email">Email<br>marcus@hpbllc-mail.com</div>
    </div>
  </section>

  <section class="card back">
    <h2 class="help-title">We Help <span>Homeowners</span></h2>

    <svg class="service-icon" style="left:56px" width="60" height="57" viewBox="0 0 60 57"><path d="M0 0H60V40L30 57L0 40Z" fill="#f57c12"/><path d="M16 27L30 15L44 27M20 24V39H40V24" fill="none" stroke="#fff" stroke-width="2"/><rect x="23" y="28" width="6" height="6" fill="none" stroke="#fff" stroke-width="1.5"/><rect x="32" y="29" width="5" height="10" fill="none" stroke="#fff" stroke-width="1.5"/></svg>
    <svg class="service-icon" style="left:178px" width="60" height="57" viewBox="0 0 60 57"><path d="M0 0H60V40L30 57L0 40Z" fill="#f57c12"/><rect x="21" y="14" width="18" height="24" fill="none" stroke="#fff" stroke-width="2"/><path d="M25 21H35M25 26H35M25 31H32" stroke="#fff" stroke-width="1.6"/></svg>
    <svg class="service-icon" style="left:300px" width="60" height="57" viewBox="0 0 60 57"><path d="M0 0H60V40L30 57L0 40Z" fill="#f57c12"/><path d="M14 28L22 22L30 27L38 22L46 28M22 22L30 34L38 22" fill="none" stroke="#fff" stroke-width="2" stroke-linejoin="round"/><path d="M25 16L30 11L35 16" fill="none" stroke="#fff" stroke-width="1.8"/></svg>

    <svg class="connector" style="left:121px" width="52" height="14" viewBox="0 0 52 14"><path d="M3 11Q26 -6 49 11" fill="none" stroke="#999" stroke-width="1.2"/><circle cx="3" cy="11" r="1.8" fill="#999"/><circle cx="49" cy="11" r="1.8" fill="#999"/></svg>
    <svg class="connector" style="left:243px;top:104px" width="52" height="14" viewBox="0 0 52 14"><path d="M3 3Q26 20 49 3" fill="none" stroke="#999" stroke-width="1.2"/><circle cx="3" cy="3" r="1.8" fill="#999"/><circle cx="49" cy="3" r="1.8" fill="#999"/></svg>

    <p class="service-label" style="left:88px">Explore options to stay in their home</p>
    <p class="service-label" style="left:208px;width:90px;margin-left:-45px">Stop or delay foreclosure</p>
    <p class="service-label" style="left:333px;width:110px;margin-left:-55px">Sell quickly for a fair price if needed</p>

    <div class="section-rule"></div>
    <div class="section-split"></div>
    <div class="agent-photo" role="img" aria-label="Portrait photo of the realtor"></div>
    <div class="agent-name">Marcus Fennimore</div>
    <p class="agent-bio">Licensed Realtor with Copperleaf Homes Realty in Bethesda, Maryland.</p>
    <p class="promise">No pressure.<br>No obligation.<br>Just real solutions tailored to your situation.</p>

    <div class="skyline-panel" role="img" aria-label="Faint light grey city skyline silhouette"></div>
    <svg class="phone-icon" width="37" height="35" viewBox="0 0 38 36"><path d="M0 0H38V26L19 36L0 26Z" fill="#f57c12"/><path d="M13 9c-2 1-3 3-1 7s6 8 9 9c2 1 4 0 5-2l-3-3-2 1c-2-1-4-3-5-5l1-2z" fill="#fff"/></svg>
    <div class="phone">(240) 558-2094</div>
    <div class="phone-rule"></div>
    <svg class="pin" width="18" height="17" viewBox="0 0 18 17"><path d="M0 0H18V12L9 17L0 12Z" fill="#f57c12"/><circle cx="9" cy="7" r="3.2" fill="none" stroke="#fff" stroke-width="1.6"/></svg>
    <div class="address">7200 Bramwick Lane, Ellicott City, MD 21043</div>

    <div class="stamp-box"></div>
    <div class="mail-line" style="top:202px"></div>
    <div class="mail-line" style="top:248px"></div>
    <div class="mail-line" style="top:294px"></div>
    <div class="mail-line" style="top:340px"></div>

    <div class="brand">
      <div class="name">HARBOR PATH PARTNERS</div>
      <div class="llc">LLC</div>
    </div>
  </section>
</div>
</body>
</html>
```